App for Basket Haven to Link to Our Site and do simple things

After Simple design that acts as an interface for our customers. the app does simple things.

*Links to our Webpage - www.baskethaven.com.au
Shopping cart will live on our website

*People can call us from App - 1800 742 918
*People can send us a message from App
*We can Send Push Notifications
*Page dedicated to specials

*Link to Diary/Calendar (or create a inbuilt calendar) to remind people of upcoming birthdays/Anniversaries*** Reminder set 7 to 15 days before event to give enough time to send a gift.

Target Market(s)

People can download the app so they have our details handy on their phone

Industry/Entity Type

Retail

Colors

Designer to choose colors to be used in the design.

Requirements
Must have
• *** PREFER AN APP DESIGNER WHO CAN CODE THE APP AS WELL***
• Link to Diary/Calendar (or create a inbuilt calendar) to remind people of upcoming birthdays/Anniversaries*** Reminder set 7 to 15 days before event to give enough time to send a gift.
• Need to be able to send push notifications with special coupon codes
• Need to be able to send Push notifications
• Our Logo/as it or modified
• a map for directions 518 Tallowgate Road, West Brunswick VIC 3055
• Need to be able to change the Banner as needed

```html
<!DOCTYPE html>
<html lang="en">
<head>
<meta charset="utf-8">
<title>Basket Haven – Home</title>
<link href="https://fonts.googleapis.com/css2?family=Montserrat:wght@400;500;600&family=Oswald:wght@300;400&display=swap" rel="stylesheet">
<style>
  :root {
    --stage: #6b6b6b;
    --screen: #f2f2f2;
    --surface: #ffffff;
    --navy: #233a8c;
    --ink: #1a1a1a;
    --muted-ink: #5a5f7a;
    --price: #e8413c;
    --old-price: #a8a8a8;
    --icon: #666666;
    --badge: #ef2b45;
    --shadow: 0 2px 5px rgba(0,0,0,0.12);
  }
  * { box-sizing: border-box; margin: 0; padding: 0; }
  html, body { width: 789px; height: 1200px; overflow: hidden; background: var(--stage); }
  a { text-decoration: none; color: inherit; }
  .app-screen {
    position: absolute; left: 57px; top: 0;
    width: 675px; height: 1200px;
    background: var(--screen);
    overflow: hidden;
  }
  .top-bar { position: absolute; left: 0; top: 0; width: 100%; height: 130px; }
  .menu-button { position: absolute; left: 31px; top: 70px; width: 36px; height: 26px; }
  .screen-title {
    position: absolute; left: 0; right: 0; top: 66px;
    text-align: center;
    font: 400 27px "Montserrat", sans-serif;
    letter-spacing: 3px;
    color: var(--muted-ink);
  }
  .search-button { position: absolute; right: 38px; top: 62px; width: 40px; height: 40px; }

  .call-bar {
    position: absolute; left: 31px; top: 139px; width: 607px; height: 69px;
    background: var(--surface);
    box-shadow: var(--shadow);
    display: flex; align-items: center; justify-content: center; gap: 16px;
    text-decoration: none;
  }
  .call-bar svg { width: 36px; height: 36px; margin-right: 14px; }
  .call-label { font: 300 26px "Oswald", sans-serif; letter-spacing: 2px; color: var(--muted-ink); }
  .call-number { font: 500 26px "Montserrat", sans-serif; color: var(--ink); margin-left: 10px; }

  .product-grid {
    position: absolute; left: 31px; top: 234px;
    display: grid; grid-template-columns: 297px 297px; column-gap: 13px; row-gap: 16px;
  }
  .product-card {
    position: relative; width: 297px; height: 416px;
    background: var(--surface); box-shadow: var(--shadow);
  }
  .product-photo {
    position: absolute; left: 22px; top: 20px; width: 253px; height: 220px;
    border-radius: 4px;
  }
  .photo-a { background: linear-gradient(135deg, #d99a4a 0%, #2b2f3a 55%, #3b6fb0 100%); }
  .photo-b { background: linear-gradient(160deg, #6b2a1c 0%, #c9a46a 55%, #e8d9b8 100%); }
  .photo-c { background: linear-gradient(135deg, #c8322a 0%, #2a2a2a 50%, #d8c06a 100%); }
  .photo-d { background: linear-gradient(135deg, #2a4a9a 0%, #2b2b2b 50%, #6a4a9a 100%); }
  .product-name {
    position: absolute; left: 29px; top: 254px;
    font: 300 25px/35px "Oswald", sans-serif;
    letter-spacing: 2.5px; color: var(--muted-ink);
  }
  .price-row { position: absolute; left: 29px; right: 0; top: 347px; height: 38px; display: flex; align-items: center; }
  .price-now { font: 400 23px "Oswald", sans-serif; letter-spacing: 1px; color: var(--price); }
  .price-was {
    font: 400 15px "Oswald", sans-serif; color: var(--old-price);
    text-decoration: line-through; margin-left: 20px;
  }
  .add-to-cart {
    position: absolute; right: 0; top: 0; width: 78px; height: 38px;
    background: var(--navy); color: #fff; border: 0; border-radius: 3px 0 0 3px;
    font: 400 13px "Oswald", sans-serif;
  }

  .tab-bar {
    position: absolute; left: 0; bottom: 0; width: 100%; height: 88px;
    background: var(--surface);
  }
  .tab-bar svg { position: absolute; top: 22px; width: 46px; height: 46px; }
  .tab-home { left: 42px; }
  .tab-mail { left: 214px; }
  .tab-alerts { left: 400px; }
  .tab-cart { left: 565px; }
  .alert-badge {
    position: absolute; left: 427px; top: 16px; width: 29px; height: 29px; border-radius: 50%;
    background: var(--badge); color: #fff; text-align: center;
    font: 500 16px/29px "Montserrat", sans-serif;
  }
</style>
</head>
<body>
<main class="app-screen">
  <header class="top-bar">
    <svg class="menu-button" viewBox="0 0 36 26" aria-label="Menu">
      <path d="M0 2H36M0 13H26M0 24H36" stroke="#222" stroke-width="3"/>
    </svg>
    <h1 class="screen-title">Home</h1>
    <svg class="search-button" viewBox="0 0 40 40" aria-label="Search">
      <circle cx="17" cy="17" r="14" fill="none" stroke="#222" stroke-width="3"/>
      <path d="M27 27L38 38" stroke="#222" stroke-width="3" stroke-linecap="round"/>
    </svg>
  </header>

  <a class="call-bar" href="tel:1800742918">
    <svg viewBox="0 0 24 24" aria-hidden="true">
      <path d="M6.6 2.5l3 3.8-1.9 2.4c1.3 2.8 3.6 5.1 6.6 6.6l2.4-1.9 3.8 3-2.2 3.1C10.7 19.3 4.7 13.3 3.5 4.7z" fill="none" stroke="#ef5a6a" stroke-width="1.4" stroke-linejoin="round"/>
    </svg>
    <span class="call-label">Call me</span>
    <span class="call-number">1800 742 918</span>
  </a>

  <section class="product-grid">
    <article class="product-card">
      <div class="product-photo photo-a" role="img" aria-label="Photo of a gourmet hamper with boxed treats, jars and a gift box"></div>
      <h2 class="product-name">Gourmet Hamper<br>(BH2409)</h2>
      <div class="price-row"><span class="price-now">$125.00</span><span class="price-was">$125.00</span><button class="add-to-cart">Add to Cart</button></div>
    </article>
    <article class="product-card">
      <div class="product-photo photo-b" role="img" aria-label="Photo of a hamper basket with sauce jars and wrapped goods"></div>
      <h2 class="product-name">Gourmet Hamper<br>(BH2409)</h2>
      <div class="price-row"><span class="price-now">$125.00</span><span class="price-was">$125.00</span><button class="add-to-cart">Add to Cart</button></div>
    </article>
    <article class="product-card">
      <div class="product-photo photo-c" role="img" aria-label="Photo of a hamper with chocolates, snacks and a ribboned gift box"></div>
      <h2 class="product-name">Gourmet Hamper<br>(BH2409)</h2>
      <div class="price-row"><span class="price-now">$125.00</span><span class="price-was">$125.00</span><button class="add-to-cart">Add to Cart</button></div>
    </article>
    <article class="product-card">
      <div class="product-photo photo-d" role="img" aria-label="Photo of a hamper with a bottle, shaker, crackers and chocolates"></div>
      <h2 class="product-name">Gourmet Hamper<br>(BH2409)</h2>
      <div class="price-row"><span class="price-now">$125.00</span><span class="price-was">$125.00</span><button class="add-to-cart">Add to Cart</button></div>
    </article>
  </section>

  <nav class="tab-bar">
    <svg class="tab-home" viewBox="0 0 46 46" aria-label="Home">
      <path d="M23 5L3 22h6v20h10V30h8v12h10V22h6z" fill="#2a4bb0"/>
    </svg>
    <svg class="tab-mail" viewBox="0 0 46 46" aria-label="Messages">
      <rect x="2" y="10" width="42" height="28" fill="none" stroke="#666" stroke-width="2"/>
      <path d="M2 10l21 17 21-17M2 38l15-14M44 38L29 24" fill="none" stroke="#666" stroke-width="2"/>
    </svg>
    <svg class="tab-alerts" viewBox="0 0 46 46" aria-label="Notifications">
      <path d="M23 6c-7 0-11 5-11 12v9l-5 7h32l-5-7v-9c0-7-4-12-11-12z" fill="none" stroke="#666" stroke-width="2" stroke-linejoin="round"/>
      <path d="M18 38a5 5 0 0 0 10 0" fill="none" stroke="#666" stroke-width="2"/>
    </svg>
    <span class="alert-badge">4</span>
    <svg class="tab-cart" viewBox="0 0 46 46" aria-label="Cart">
      <path d="M2 8h7l5 22h24l5-17H12" fill="none" stroke="#666" stroke-width="2" stroke-linejoin="round"/>
      <path d="M15 18h25M16 24h21" stroke="#666" stroke-width="2"/>
      <circle cx="18" cy="37" r="3" fill="none" stroke="#666" stroke-width="2"/>
      <circle cx="34" cy="37" r="3" fill="none" stroke="#666" stroke-width="2"/>
    </svg>
  </nav>
</main>
</body>
</html>
```